Dog Grooming Provisions - Fur Refresher Spray *

We are Willow Bend Meadows. A city dog's country camp. We are a dog services company providing a camp experience in Upstate NY to the dogs of NYC. We are creating a hand made fur refresher spray for our clients (who are dogs!) for the holidays.
These labels will be used on a 4 ounce vintage style spray bottles. The design should have a vintage grooming provisions feel. We'd like to see the design be a simple, vintage style black with white, charcoal, or very dark almost black green.
The design should incorporate our varying vintage fonts, our logo with "grooming provisions" all natural & handmade, Fur Refresh
Obviously this is a gift and while Fur Refresh is important, our brand should be a focus. Perhaps a very simple and "elegant" bone but steer away from paws and pet cheesy! Classic, vintage and camp.

Target Market(s)

Upscale Pet Owners of NYC

Industry/Entity Type

Pet Care

Logo Text

Willow Bend Meadows Dog Camp (Dog Camp is is for logo not necessary for label)

Font styles to use
Serif
Sans Serif
Script

Colors
9bcb3b
000000
5c5c5c

Requirements
Must have
• I am looking for a black and white or very simple design. I'd even like our logo for this use be black/white (if possible? - not sure if that can happen?)
• Our branding! Simple vintage feel.
• Grooming Provisions
• Fur Refresher or Fur Refresh or Fur Fresh Spray
• Handmade
• All Natural
• Fonts of vintage style - varying with simple and bold (i attached some photos)
Nice to have
• **MAYBE a very Simple Bone (see drawing) - very very thin.
Should not have
• 1. PAWS or cheap looking dog related items
• 2. No bright colors - truly prefer black and white or black with intention to print on plain pulp/brown paper (attached photo)
• 3. Over designed

```html
<!DOCTYPE html>
<html lang="en">
<head>
<meta charset="utf-8">
<title>Willow Bend Meadows – Fur Refresher Label</title>
<link rel="stylesheet" href="https://fonts.googleapis.com/css2?family=Barlow:wght@400;500&family=Damion&family=Great+Vibes&family=Russo+One&display=swap">
<style>
  :root {
    --ink: #1c1c1c;
    --paper: #ffffff;
    --brand-green: #1f4d3a;
  }
  html, body {
    margin: 0;
    padding: 0;
    overflow: hidden;
    background: var(--paper);
  }
  .label {
    position: relative;
    width: 998px;
    height: 1200px;
    background: var(--paper);
    color: var(--ink);
    overflow: hidden;
  }
  .label-frame {
    position: absolute;
    inset: 0;
  }
  .brand-mark {
    position: absolute;
    left: 0;
    width: 998px;
    top: 130px;
    display: flex;
    flex-direction: column;
    align-items: center;
    gap: 36px;
    font-family: "Barlow", sans-serif;
    font-weight: 500;
    font-size: 54px;
    line-height: 1;
    letter-spacing: 1px;
    color: var(--brand-green);
  }
  .brand-mark .seal {
    width: 200px;
    height: 200px;
    border-radius: 50%;
    background: var(--brand-green);
  }
  .centered {
    position: absolute;
    left: 0;
    width: 998px;
    text-align: center;
    line-height: 1;
    white-space: nowrap;
  }
  .tagline {
    top: 532px;
    font-family: "Barlow", sans-serif;
    font-size: 44px;
    font-weight: 400;
  }
  .brand-script {
    top: 590px;
    font-family: "Great Vibes", cursive;
    font-size: 104px;
  }
  .product-name {
    top: 752px;
    font-family: "Russo One", sans-serif;
    font-size: 100px;
    letter-spacing: 6px;
  }
  .product-name .small {
    font-size: 78px;
  }
  .claims {
    top: 910px;
    font-family: "Damion", cursive;
    font-size: 62px;
  }
  .established {
    top: 1010px;
    font-family: "Barlow", sans-serif;
    font-size: 42px;
  }
</style>
</head>
<body>
  <div class="label">
    <svg class="label-frame" width="998" height="1200" viewBox="0 0 998 1200" aria-hidden="true">
      <path d="M56 36 H940 A32 32 0 0 0 972 68 V1132 A32 32 0 0 0 940 1164 H56 A32 32 0 0 0 24 1132 V68 A32 32 0 0 0 56 36 Z"
            fill="none" stroke="var(--ink)" stroke-width="7"/>
      <rect x="70" y="84" width="858" height="1032" fill="none" stroke="var(--ink)" stroke-width="2"/>
      <line x1="122" y1="722" x2="876" y2="722" stroke="var(--ink)" stroke-width="3"/>
      <line x1="122" y1="892" x2="876" y2="892" stroke="var(--ink)" stroke-width="3"/>
    </svg>

    <div class="brand-mark"><span class="seal"></span>Willow Bend Meadows</div>

    <div class="centered tagline">Grooming • Provisions</div>
    <div class="centered brand-script">willow bend meadows</div>
    <div class="centered product-name">F<span class="small">UR</span> R<span class="small">EFRESHER</span></div>
    <div class="centered claims">hand made / all natural</div>
    <div class="centered established">*est 2005*</div>
  </div>
</body>
</html>
```